Gutschein für einen Friseursalon
Zielgruppe
Wir bieten die klassische Bandbreite von Haarschnitten und Friseurdienstleistungen an. Unsere Kunden finden sich im alternativen Stadtteil Friedrichshain in Berlin und sind zwischen 20 und 50 Jahren alt. Unser Salon ist im Vintage-Stil dekoriert. Impressionen finden Sie unter www.friseur-olvenau.de
Aufgabenstellung
Wir benötigen einen Gutschein, den unsere Kunden verschenken können. Dieser soll in der Höhe des Preises individuell dem Kundenwunsch angepasst werden können (also keinen vorgedruckten Wert haben).
Die Maße des Gutscheines erbitten wir in DIN lang (21 x 9,8 cm) im Querformat.
Beim Gutscheinverkauf erhält der Kunden einen Bonausdruck mit Barcode, der an den Gutschein angeheftet wird. Hierfür sollte es einen eigenen Bereich geben, sodass alle anderen Informationen nicht verdeckt werden. Der Ausdruck hat eine Breite von 80 mm).
Weiter Pflichtangaben, welche auf dem Gutschein enthalten sein sollen:
- Datum
- Unterschrift
- Gutscheinwert
- Logo
- Webseite
- Öffnungszeiten und Telefonnummer
- Hinweis auf die Möglichkeit zur Online-Buchung auf unserer Webseite
Ich habe diesem Projekt unser Logo und unsere Visitenkarte beigefügt. Diese sollen sich optisch im Gutschein natürlich wiederfinden.
Ich bin für alle Vorschläge der weiteren Gestaltung offen. Gerne auch für eine klappbare Version des Gutscheines.
Der Gutschein soll letztendlich bei Blattkurier.de gedruckt werden. Bitte beachten Sie bei der Erstellung die entsprechenden Vorgaben der Druckdaten.

```html
<!DOCTYPE html>
<html lang="de">
<head>
<meta charset="utf-8">
<title>Gutschein – Friseur Olvenau</title>
<link rel="stylesheet" href="https://fonts.googleapis.com/css2?family=Bebas+Neue&family=Oswald:wght@300&display=swap">
<style>
  :root {
    --ink: #1e1e1e;
    --gold-light: #fbe8a6;
    --gold-mid: #f6dc8e;
    --gold-deep: #efcb72;
    --paper: #ffffff;
    --frame: #2a2a2a;
    --handle: #8a8a8a;
  }
  * { margin: 0; padding: 0; box-sizing: border-box; }
  html, body { width: 1200px; height: 560px; overflow: hidden; background: var(--paper); }
  .voucher {
    position: relative;
    width: 1200px; height: 560px;
    border: 1px solid var(--frame);
    overflow: hidden;
    color: var(--ink);
    font-family: "Bebas Neue", "Oswald", sans-serif;
  }
  .front {
    position: absolute; left: 0; top: 0;
    width: 749px; height: 100%;
  }
  .front__pattern {
    position: absolute; inset: 0;
    background: radial-gradient(ellipse at 50% 45%, var(--gold-light) 0%, var(--gold-mid) 60%, var(--gold-deep) 100%);
  }
  .front__title {
    position: absolute; left: 0; width: 740px; top: 36px;
    text-align: center; font-size: 68px; line-height: 1; letter-spacing: 0.5px;
  }
  .front__district {
    position: absolute; left: 0; width: 744px; top: 150px;
    text-align: center; font-size: 33px; line-height: 1;
  }
  .brand-name {
    position: absolute; left: 0; width: 757px; top: 192px;
    text-align: center; font-size: 108px; line-height: 1; letter-spacing: 1px;
  }
  .fields {
    position: absolute; left: 77px; top: 408px; width: 603px;
    border-top: 2px solid var(--ink);
    height: 30px;
    font-family: "Oswald", sans-serif; font-weight: 300; font-size: 15px;
  }
  .fields span { position: absolute; top: 8px; }
  .fields__value { left: 0; }
  .fields__date { left: 448px; }
  .fields__signature { right: 0; }
  .booking {
    position: absolute; left: 70px; width: 604px; text-align: center;
  }
  .booking--note {
    top: 478px; font-family: "Oswald", sans-serif; font-weight: 300; font-size: 20px; letter-spacing: -0.3px;
  }
  .booking--hint {
    top: 506px; font-size: 23.5px; line-height: 1;
  }
  .booking__arrow { position: absolute; left: 680px; top: 481px; }
  .back {
    position: absolute; left: 749px; top: 0; width: 451px; height: 100%;
    background: var(--paper);
  }
  .back__handle {
    position: absolute; left: 204px; top: 28px; width: 57px; height: 6px;
    border-radius: 3px; background: var(--handle);
  }
  .back__text {
    position: absolute; left: 73px; top: 63px; width: 307px;
    font-size: 27.5px; line-height: 29px; text-align: justify;
    text-transform: uppercase; hyphens: auto;
  }
</style>
</head>
<body>
<main class="voucher">
  <section class="front">
    <div class="front__pattern" role="img" aria-label="Goldenes Damast-Ornamentmuster im Vintage-Stil"></div>
    <h1 class="front__title">Gutschein</h1>
    <p class="front__district">- Friedrichshain, Berlin -</p>
    <p class="brand-name">Friseur Olvenau</p>
    <div class="fields">
      <span class="fields__value">Gutscheinwert</span>
      <span class="fields__date">Datum</span>
      <span class="fields__signature">Unterschrift</span>
    </div>
    <p class="booking booking--note">Ihr könnt uns auch rund um die Uhr online über unsere Website buchen</p>
    <p class="booking booking--hint">Unter dem Bon findet ihr alles was ihr schon immer über uns wissen wolltet</p>
    <svg class="booking__arrow" width="40" height="46" viewBox="0 0 40 46" aria-hidden="true">
      <polygon points="0,0 40,23 0,46" fill="var(--ink)"/>
    </svg>
  </section>
  <section class="back">
    <div class="back__handle"></div>
    <p class="back__text" lang="la">Lorem ipsum dolor sit amet, consectetuer adipiscing elit. Aenean commodo ligula eget dolor. Aenean massa. Cum sociis natoque penatibus et magnis dis parturient montes, nascetur ridiculus mus. Donec quam felis, ultricies nec, pellentesque eu, pretium quis, sem. Nulla consequat massa quis enim. Donec pede justo, fringilla vel, aliquet nec, vulputate eget, arcu. In enim justo, rhoncus ut, imperdiet a, venenatis vitae, justo. Nullam dictum felis eu pede mollis pretium. Integer tincidunt. Cras dapibus. Vivamus elementum semper nisi. Aenean vulputate eleifend tellus. Aenean leo</p>
  </section>
</main>
</body>
</html>
```